Crumb Joy pastry business card design

I need a logo and a business card design for my baking business, "Crumb Joy". I daily bake French pastries from scratch using high quality ingredients and directly cater to local customers. My product is very authentic but sold at a casual setting . I'm looking for a simple, cute, stylish yet earthy design. Like this kind of feel:
http://clipvista.example/71946302
Target Market(s)
Metropolitan food conscious consumers in their 20-40s
Industry/Entity Type
Business
Requirements
Must have
- Soft pastel colors or other types of color schemes that would remind French pastries.
email: welovecrumbles@mailnest.example
twitter@bitemesf
www.crumbjoyla.example
Nice to have
Should not have
- pictures of pastries - sketches are ok.

```html
<!DOCTYPE html>
<html lang="en">
<head>
<meta charset="utf-8">
<title>Crumb Joy – Business Card</title>
<link rel="stylesheet" href="https://fonts.googleapis.com/css2?family=Poiret+One&display=swap">
<style>
  :root {
    --canvas-bg: #efe9e1;
    --card-brown: #3b1f1e;
    --cream: #e4e1cc;
    --photo-light: #c9ad92;
    --photo-mid: #a0826a;
    --photo-dark: #4e3426;
    --logo-white: #ffffff;
    --shadow: rgba(40, 24, 16, 0.22);
  }
  * { box-sizing: border-box; margin: 0; padding: 0; }
  html, body {
    width: 1200px;
    height: 880px;
    overflow: hidden;
    background: var(--canvas-bg);
  }
  .canvas {
    position: relative;
    width: 1200px;
    height: 880px;
    font-family: "Poiret One", sans-serif;
  }
  .card {
    position: absolute;
    top: 286px;
    width: 540px;
    height: 308px;
    overflow: hidden;
    box-shadow: 0 10px 26px var(--shadow);
  }

  /* Back: contact side */
  .card--back {
    left: 40px;
    background: var(--card-brown);
    color: var(--cream);
  }
  .contact-list {
    list-style: none;
    position: absolute;
    left: 56px;
    top: 84px;
    right: 24px;
  }
  .contact-item {
    display: flex;
    align-items: center;
    height: 44px;
    font-size: 20px;
    letter-spacing: 0.07em;
    text-transform: uppercase;
    white-space: nowrap;
  }
  .contact-icon {
    width: 22px;
    height: 22px;
    margin-right: 20px;
    flex: none;
  }
  .contact-icon--blank {
    display: inline-block;
  }
  .corner-ornament {
    position: absolute;
    right: 0;
    bottom: 0;
    width: 104px;
    height: 80px;
    background: var(--cream);
  }

  /* Front: logo side */
  .card--front {
    left: 620px;
  }
  .front-photo {
    position: absolute;
    inset: 0;
    background:
      radial-gradient(ellipse 42% 55% at 78% 62%, var(--photo-dark) 0%, #6b4a36 60%, transparent 100%),
      linear-gradient(120deg, var(--photo-light) 0%, var(--photo-mid) 55%, #7a5b47 100%);
  }
  .brand {
    position: absolute;
    inset: 0;
    display: flex;
    flex-direction: column;
    align-items: center;
    justify-content: center;
    color: var(--logo-white);
  }
  .brand-name {
    font-size: 58px;
    letter-spacing: 0.14em;
    text-transform: uppercase;
    line-height: 1;
  }
  .brand-url {
    margin-top: 22px;
    font-size: 18px;
    letter-spacing: 0.1em;
    text-transform: uppercase;
  }
</style>
</head>
<body>
<main class="canvas">

  <section class="card card--back" aria-label="Business card, contact side">
    <ul class="contact-list">
      <li class="contact-item">
        <svg class="contact-icon" viewBox="0 0 22 22" aria-hidden="true">
          <rect x="2" y="5" width="18" height="12" fill="none" stroke="var(--cream)" stroke-width="1.5"/>
          <polyline points="2,5 11,12 20,5" fill="none" stroke="var(--cream)" stroke-width="1.5"/>
        </svg>
        welovecrumbles@mailnest.example
      </li>
      <li class="contact-item">
        <span class="contact-icon contact-icon--blank" aria-hidden="true"></span>
        @crumbjoyla
      </li>
      <li class="contact-item">
        <svg class="contact-icon" viewBox="0 0 22 22" aria-hidden="true">
          <circle cx="11" cy="11" r="9" fill="none" stroke="var(--cream)" stroke-width="1.5"/>
          <ellipse cx="11" cy="11" rx="4" ry="9" fill="none" stroke="var(--cream)" stroke-width="1.2"/>
          <line x1="2" y1="11" x2="20" y2="11" stroke="var(--cream)" stroke-width="1.2"/>
        </svg>
        www.crumbjoyla.example
      </li>
    </ul>
    <div class="corner-ornament" role="img" aria-label="Decorative scalloped cream ornament in the corner"></div>
  </section>

  <section class="card card--front" aria-label="Business card, logo side">
    <div class="front-photo" role="img" aria-label="Photograph of a chocolate tart on a lace doily with a fork beside it"></div>
    <div class="brand">
      <p class="brand-name">Crumb Joy</p>
      <p class="brand-url">www.crumbjoyla.example</p>
    </div>
  </section>

</main>
</body>
</html>
```